a Label for a candle jar and its gift box

I would like a label that is modern minimalist for candles jars. These jars are colored as white, amber and black. I am thinking maybe foiling gold/silver background with logo only and maybe company name in different color that suits the foiling background color/s. I would like a high quality luxurious design that shows the preciousness of this candle. I am open to any ideas you might have for the design but so far I have used a logo only on the jar which I really like BUT I still feel that it is not enough branding for people when you only show them the logo so I am considering adding the business name. Again, I am open to both ideas (with logo only or logo with business name (Velvet Lantern).

IMPORTANT: YOU MAY IGNORE MY DESIGN COMPLETELY AND DO YOUR OWN ONE AS LONG AS YOU KERP THE LOGO DESIGN. YOU MAY ALSO ADJUST THE LOGO A BIT TO SUIT YOUR DESIGN. - sorry im using capital letters to show importance but im not yelling :)
Updates

UPDATE: To clarify, I have uploaded a video called Corvale in the box to show what the current product look like. It is a corvale jar with a logo only and the jar box has a window that shows the jar with the logo on it and the back of that jar box has a bigger version of the label that has more details (i.e. Fragrance name and website link). So to make it clear, I would like to have two versions of the lables: 1. on the jar with minimal info (logo only or logo with the business name) 2. Bigger version of the label with more info to put on the back of the jar box - as described above. The dimensions of the jars are as per this link https://www.plintova.com.au/corvale-medium-base-and-flat-lid-amber-packed-with-lid-on/ The dimensions of the jar box as per this link https://www.plintova.com.au/corvale-medium-flat-lid-candle-box-with-window-beige/ Looking forward to some artistic productions :)

Update #2: Tues 25 Dec 18 1. I have uploaded the photo which has the logo with the name 'Velvet Lantern' below it just for a reference. However, I would like the designer to modify the current font and NOT to use it as the word 'of in the phrase 'Velvet Lantern' does not come out clear enough after printing. 2. I would like the designer NOT to create a design that will require a clear sticker/label for printing. 3. I have attached the photos of my current designs on the jars or the jar box just as a reference but please do NOT just use the same fonts and only change background. I am hoping to see something different and more professional than my own design :) Thank you very much!

Font styles to use
Decorative
Script

Requirements
Must have
• I would like them to fit on the three colors of the jars below - white, amber and black. Below is a link to how the jar looks like https://www.plintova.com.au/candle-making-supplies/candle-jars/corvale-candle-jars/?glassware_colour=415,443,417&glassware_size=268
Nice to have
• I would like to have a modern design which is suitable for both feminine and musculine.
Should not have
• shouldnt have so much writing on it!

```html
<!DOCTYPE html>
<html lang="en">
<head>
<meta charset="utf-8">
<title>Velvet Lantern – Turkish Rose box and jar labels</title>
<link rel="stylesheet" href="https://fonts.googleapis.com/css2?family=Allura&family=Josefin+Sans:wght@400&display=swap">
<style>
  :root {
    --canvas: #ffffff;
    --box-black: #1f1f1f;
    --ink: #141414;
    --paper: #ffffff;
  }
  * { margin: 0; padding: 0; box-sizing: border-box; }
  html, body {
    width: 1200px;
    height: 849px;
    overflow: hidden;
    background: var(--canvas);
  }
  .artboard {
    position: relative;
    width: 1200px;
    height: 849px;
  }

  /* Box back label */
  .box-face {
    position: absolute;
    left: 184px;
    top: 141px;
    width: 421px;
    height: 549px;
    background: var(--box-black);
  }
  .box-label {
    position: absolute;
    left: 57px;
    top: 136px;
    width: 310px;
    height: 317px;
    border: 3px solid var(--paper);
    padding: 5px;
  }
  .box-label__inner {
    width: 100%;
    height: 100%;
    border: 6px solid var(--paper);
    padding: 2px;
  }
  .box-label__panel {
    width: 100%;
    height: 100%;
    display: flex;
    flex-direction: column;
    align-items: center;
    color: var(--paper);
    text-align: center;
  }
  .brand-name {
    font-family: "Josefin Sans", sans-serif;
    font-weight: 400;
    font-size: 16px;
    letter-spacing: 0.14em;
    text-transform: uppercase;
    margin-top: 108px;
  }
  .fragrance-name {
    font-family: "Allura", cursive;
    font-weight: 400;
    font-size: 50px;
    line-height: 1;
    margin-top: 36px;
  }
  .web-address {
    font-family: "Josefin Sans", sans-serif;
    font-weight: 400;
    font-size: 7.5px;
    letter-spacing: 0.16em;
    text-transform: uppercase;
    margin-top: auto;
    margin-bottom: 22px;
  }

  /* Jar round label */
  .jar-label {
    position: absolute;
    left: 899px;
    top: 409px;
    width: 166px;
    height: 166px;
  }
  .jar-label svg { display: block; }
  .jar-label__name {
    position: absolute;
    inset: 0;
    display: flex;
    flex-direction: column;
    align-items: center;
    justify-content: center;
    font-family: "Josefin Sans", sans-serif;
    font-weight: 400;
    font-size: 12px;
    letter-spacing: 0.16em;
    text-transform: uppercase;
    color: var(--ink);
    line-height: 1.7;
    padding-top: 6px;
  }
</style>
</head>
<body>
  <main class="artboard">
    <section class="box-face" aria-label="Gift box back label">
      <div class="box-label">
        <div class="box-label__inner">
          <div class="box-label__panel">
            <p class="brand-name">Velvet Lantern</p>
            <p class="fragrance-name">Turkish Rose</p>
            <p class="web-address">www.velvetlantern-candles.com.au</p>
          </div>
        </div>
      </div>
    </section>

    <section class="jar-label" aria-label="Round jar label">
      <svg width="166" height="166" viewBox="0 0 166 166" aria-hidden="true">
        <circle cx="83" cy="83" r="82" fill="var(--paper)" stroke="var(--ink)" stroke-width="2"/>
        <circle cx="83" cy="83" r="76" fill="none" stroke="var(--ink)" stroke-width="1.4"/>
      </svg>
      <p class="jar-label__name"><span>Velvet</span><span>Lantern</span></p>
    </section>
  </main>
</body>
</html>
```